BRISKWATER MOTION GYM FLYER DESIGN

We want a flyer designed for our gym. We have an example of a flyer which we like and I have put it into the images I have uploaded. I would like to recreate using our pictures, so its a pretty straight forward job. We also want to put our weekly timetable on the back of the flyer. We would like the size of the flyer to be A5.

Target Market(s)

FITNESS

Industry/Entity Type

Gym

Colors
33a6d7
ffffff

Requirements
Must have
• We just want to recreate the flyer but we must have the following info on the flyer and we want our timetable on the back of the flyer which you can get from this link: http://www.briskwatermotiongym.com/timetable
• Briskwater Motion Gym is a fun community of humble people. Our goal is to help guide you towards a fitter, healthier lifestyle!
• Our Programs
• HIIT
• High intensity interval training is 30-45 minutes of fat burning fun. The class is a mix of cardio, bodyweight and some resistance movements.
• Conditioning
• A full hour of strength, cardio and bodyweight training to get you in tip top shape. Expect a mix of barbells, kettlebells, rowing machines, bikes and other training methods.
• KPL
• This is our big Friday session to set you up for the weekend. 90 minutes of hard training that is done with a team emphasis. From heavy lifting to cardio triathlons, this class has it all but not for the faint hearted.
• Muay Thai
• Commonly known as the science of 8 limbs you will learn how to punch, kick, knee and elbow. Thailands national sport is a great way to get your fitness kick. We train the complete beginner all the way to international fighters so you are in great hands.
• Kids Muay Thai
• Our junior program starts from age 6 onwards. Muay Thai is a great way for kids to get active and fit while learning new skills. Training in martial arts also teaches self discipline and socialisation skills.
• Yoga
• A combination of physical and mental practises that will leave you focused and refreshed for whatever the week throws at you. We always recommend our yoga classes as a great way to balance the high intensity training we offer.
• U-Press
• Strength training with a little bit of conditioning. We regularly update the program and re test lifts to ensure you are making progress and getting stronger.
• CONTACT US
• OUR LOCATION:
• Unit 42C
• 273 Quillan Street
• Fenwick Hollow
• Glasgow
• G72TR
• Phone: 07950362814
• Email: info@briskwatermotiongym.com
• Web: www.briskwatermotiongym.com
Nice to have
• Can use all the picture but if not be good to use the boxing one and the group training one.

```html
<!DOCTYPE html>
<html lang="en">
<head>
<meta charset="utf-8">
<title>Briskwater Motion Gym – Flyer</title>
<link href="https://fonts.googleapis.com/css2?family=Open+Sans:ital,wght@0,400;0,600;0,700;1,300&family=Oswald:wght@500;600&display=swap" rel="stylesheet">
<style>
  :root {
    --brand-blue: #33a6d7;
    --brand-blue-deep: #1f8cc0;
    --row-tint: #e4f2f9;
    --rule: #c4e1ef;
    --white: #ffffff;
    --stage: #eef1f3;
  }
  * { box-sizing: border-box; margin: 0; padding: 0; }
  html, body { width: 1200px; height: 928px; overflow: hidden; background: var(--stage); }
  body { position: relative; font-family: "Open Sans", sans-serif; }

  .flyer {
    position: absolute; top: 82px;
    width: 540px; height: 764px;
    overflow: hidden;
    box-shadow: 0 6px 24px rgba(0,0,0,.18);
    color: var(--white);
  }
  .flyer--front { left: 40px; background: var(--brand-blue); }
  .flyer--back { left: 620px; background: var(--white); }
  .flyer__shapes { position: absolute; left: 0; top: 0; }

  /* front */
  .intro {
    position: absolute; left: 20px; top: 28px; width: 196px;
    font-style: italic; font-weight: 300; font-size: 18px; line-height: 1.3;
  }
  .intro::before { content: "\201C"; font-weight: 700; font-style: normal; font-size: 26px; line-height: 0; vertical-align: -7px; margin-right: 2px; }
  .programs { position: absolute; left: 204px; top: 240px; width: 322px; }
  .programs__title {
    font-family: "Oswald", sans-serif; font-weight: 600; font-size: 30px; line-height: 1.2;
    letter-spacing: 1px; margin-bottom: 8px;
  }
  .program { position: relative; padding-left: 16px; margin-bottom: 6px; }
  .program::before {
    content: ""; position: absolute; left: 0; top: 3px;
    width: 8px; height: 8px; border-radius: 50%;
    border: 2px solid var(--white);
  }
  .program__name { font-weight: 700; font-size: 11px; line-height: 14px; text-transform: uppercase; letter-spacing: .3px; }
  .program__text { font-size: 9px; line-height: 12.4px; }
  .contact {
    position: absolute; left: 16px; top: 470px; width: 160px;
    color: var(--brand-blue-deep); font-size: 9px; line-height: 1.5;
  }
  .brand { display: flex; align-items: center; gap: 8px; }
  .brand__mark { width: 12px; height: 12px; background: currentColor; flex: none; }
  .brand__name { font-weight: 700; font-size: 12px; line-height: 1.25; }
  .contact .brand { color: var(--brand-blue); margin-bottom: 16px; }
  .contact__heading { font-weight: 700; text-transform: uppercase; font-size: 10px; margin-bottom: 2px; }
  .contact__label { font-weight: 700; display: block; }
  .contact address { font-style: normal; margin-bottom: 8px; }
  .contact p { margin-bottom: 3px; }

  /* back */
  .timetable {
    position: absolute; left: 20px; top: 150px; width: 500px;
    border-collapse: collapse; table-layout: fixed;
    color: var(--brand-blue-deep); font-size: 8px; text-align: center;
  }
  .timetable th, .timetable td { height: 29px; border: 1px solid var(--rule); padding: 0 2px; line-height: 1.15; }
  .timetable thead th { background: var(--brand-blue); color: var(--white); font-weight: 700; font-size: 10px; }
  .timetable tbody th { font-weight: 700; font-size: 9px; width: 59px; }
  .timetable tbody tr:nth-child(odd) { background: var(--row-tint); }
  .timetable .time-col { width: 59px; }
  .back-band {
    position: absolute; left: 0; bottom: 0; width: 540px; height: 112px;
    background: var(--brand-blue); display: flex; align-items: center; padding-left: 30px;
  }
  .back-band .brand__name { font-size: 16px; }
</style>
</head>
<body>
<main class="flyer flyer--front">
  <svg class="flyer__shapes" width="540" height="764" viewBox="0 0 540 764">
    <rect x="226" y="0" width="314" height="230" fill="#b9746a" role="img" aria-label="Photo: boxing coach holding pads for a boxer in the ring"/>
    <rect x="0" y="230" width="190" height="100" fill="#3c4a56" role="img" aria-label="Photo: boxer in green shirt punching with orange gloves"/>
    <polygon points="0,330 190,330 188,420 0,400" fill="#5b8fa3" role="img" aria-label="Photo: group training class in the gym"/>
    <polygon points="0,400 188,420 176,764 0,764" fill="#ffffff"/>
    <polygon points="190,230 540,230 540,764 176,764" fill="#33a6d7"/>
  </svg>

  <p class="intro">Briskwater Motion Gym is a fun community of humble people. Our goal is to help guide you towards a fitter, healthier lifestyle!</p>

  <section class="programs">
    <h2 class="programs__title">OUR PROGRAMS</h2>
    <div class="program"><h3 class="program__name">HIIT</h3><p class="program__text">High intensity interval training is 30-45 minutes of fat burning fun. The class is a mix of cardio, bodyweight and some resistance movements.</p></div>
    <div class="program"><h3 class="program__name">Conditioning</h3><p class="program__text">A full hour of strength, cardio and bodyweight training to get you in tip top shape. Expect a mix of barbells, kettlebells, rowing machines, bikes and other training methods.</p></div>
    <div class="program"><h3 class="program__name">KPL</h3><p class="program__text">This is our big Friday session to set you up for the weekend. 90 minutes of hard training that is done with a team emphasis. From heavy lifting to cardio triathlons, this class has it all but not for the faint hearted.</p></div>
    <div class="program"><h3 class="program__name">Muay Thai</h3><p class="program__text">Commonly known as the science of 8 limbs you will learn how to punch, kick, knee and elbow. Thailands national sport is a great way to get your fitness kick. We train the complete beginner all the way to international fighters so you are in great hands.</p></div>
    <div class="program"><h3 class="program__name">Kids Muay Thai</h3><p class="program__text">Our junior program starts from age 6 onwards. Muay Thai is a great way for kids to get active and fit while learning new skills. Training in martial arts also teaches self discipline and socialisation skills.</p></div>
    <div class="program"><h3 class="program__name">Yoga</h3><p class="program__text">A combination of physical and mental practises that will leave you focused and refreshed for whatever the week throws at you. We always recommend our yoga classes as a great way to balance the high intensity training we offer.</p></div>
    <div class="program"><h3 class="program__name">U-Press</h3><p class="program__text">Strength training with a little bit of conditioning. We regularly update the program and re test lifts to ensure you are making progress and getting stronger.</p></div>
  </section>

  <section class="contact">
    <div class="brand"><span class="brand__mark"></span><span class="brand__name">BRISKWATER MOTION GYM</span></div>
    <h3 class="contact__heading">Our Location:</h3>
    <address>Unit 42C<br>273 Quillan Street<br>Fenwick Hollow<br>Glasgow G72TR</address>
    <p><span class="contact__label">Phone:</span> 07950362814</p>
    <p><span class="contact__label">Email:</span> info@briskwatermotiongym.com</p>
    <p><span class="contact__label">Web:</span> www.briskwatermotiongym.com</p>
  </section>
</main>

<main class="flyer flyer--back">
  <svg class="flyer__shapes" width="540" height="130" viewBox="0 0 540 130">
    <rect x="0" y="0" width="540" height="130" fill="#6fa7bd" role="img" aria-label="Photo: group training session in the gym"/>
  </svg>

  <table class="timetable">
    <thead>
      <tr><th class="time-col"></th><th>MON</th><th>TUE</th><th>WED</th><th>THU</th><th>FRI</th><th>SAT</th><th>SUN</th></tr>
    </thead>
    <tbody>
      <tr><th>6 AM</th><td>HIIT</td><td>U-Press</td><td>HIIT</td><td>U-Press</td><td>HIIT</td><td></td><td></td></tr>
      <tr><th>7 AM</th><td>Conditioning</td><td></td><td>Conditioning</td><td></td><td>Conditioning</td><td></td><td></td></tr>
      <tr><th>8 AM</th><td></td><td></td><td></td><td></td><td></td><td>HIIT</td><td></td></tr>
      <tr><th>9 AM</th><td></td><td></td><td></td><td></td><td></td><td>Muay Thai</td><td>Yoga</td></tr>
      <tr><th>10 AM</th><td>Yoga</td><td></td><td>Yoga</td><td></td><td></td><td>Kids Muay Thai</td><td></td></tr>
      <tr><th>11 AM</th><td></td><td></td><td></td><td></td><td></td><td></td><td></td></tr>
      <tr><th>12 PM</th><td>HIIT</td><td>HIIT</td><td>HIIT</td><td>HIIT</td><td>HIIT</td><td></td><td></td></tr>
      <tr><th>1 PM</th><td></td><td></td><td></td><td></td><td></td><td></td><td></td></tr>
      <tr><th>2 PM</th><td></td><td></td><td></td><td></td><td></td><td></td><td></td></tr>
      <tr><th>3 PM</th><td></td><td></td><td></td><td></td><td></td><td></td><td></td></tr>
      <tr><th>4 PM</th><td>Kids Muay Thai</td><td></td><td>Kids Muay Thai</td><td></td><td></td><td></td><td></td></tr>
      <tr><th>5 PM</th><td>U-Press</td><td>Conditioning</td><td>U-Press</td><td>Conditioning</td><td>KPL</td><td></td><td></td></tr>
      <tr><th>6 PM</th><td>Muay Thai</td><td>HIIT</td><td>Muay Thai</td><td>HIIT</td><td></td><td></td><td></td></tr>
      <tr><th>7 PM</th><td>Conditioning</td><td>Muay Thai</td><td>Yoga</td><td>Muay Thai</td><td></td><td></td><td></td></tr>
      <tr><th>8 PM</th><td></td><td>Yoga</td><td></td><td>Yoga</td><td></td><td></td><td></td></tr>
    </tbody>
  </table>

  <footer class="back-band">
    <div class="brand"><span class="brand__mark"></span><span class="brand__name">BRISKWATER MOTION GYM</span></div>
  </footer>
</main>
</body>
</html>
```